Business cards for property management company

Need new business cards designed for our property management company and rental community, Blue Fern Commons. These cards will be primarily picked up by rental applicants.

May be single or double sided design.

I need cards for two different people, listed below. The design can be the same for both, and the only information that will be different is name and email address.

Industry/Entity Type

Property Management

Requirements
Must have
• US standard business card - 2''x3.5'' horizontal design.

1. Logo (attached). The text does not have to stay below the logo, but the card does need to say "Blue Fern Commons" somewhere on it (does not have to be same font as logo, but those fonts are Americana Extra Bold and BlackJack if needed).
2. Name: one with "Paula Whitcombe" and one with "Darrell Whitcombe"
3. Email address: one with "paula@bluefernhome.com" and one with "darrell@bluefernhome.com"
4. Web address: bluefernhome.com
5. Phone: 281.604.2218
6. Address: 1783 Wexford Lane, Porterfield, Texas 77812 (zip code may me omitted, at your discretion)
Should not have
• No rounded corners or special cuts.

No bevel, emboss or shadow effects.

As a note, please do not use our website as a basis for color or design schemes. We are working on a redesign, based around the new logo (attached to brief).

```html
<!DOCTYPE html>
<html lang="en">
<head>
<meta charset="utf-8">
<title>Blue Fern Commons – Business Card</title>
<link rel="stylesheet" href="https://fonts.googleapis.com/css2?family=Open+Sans:wght@400;600;700;800&display=swap">
<style>
  :root {
    --card-white: #ffffff;
    --brand-green: #1fa04a;
    --label-blue: #1d7ea6;
    --ink: #111111;
    --accent-yellow: #d6df22;
    --wave-blue: #0b7fc6;
    --wave-teal: #0a8f98;
    --wave-lime: #a9c93c;
  }
  html, body {
    margin: 0;
    padding: 0;
    width: 1200px;
    height: 686px;
    overflow: hidden;
    background: var(--card-white);
  }
  .business-card {
    position: relative;
    width: 1200px;
    height: 686px;
    overflow: hidden;
    background: var(--card-white);
    font-family: "Open Sans", Arial, sans-serif;
  }
  .card-art {
    position: absolute;
    inset: 0;
    width: 1200px;
    height: 686px;
  }
  .brand-name {
    font-family: "Open Sans", Arial, sans-serif;
    font-weight: 700;
    font-size: 62px;
    fill: var(--brand-green);
  }
  .brand-mark { fill: var(--brand-green); }
  .field-label {
    font-family: "Open Sans", Arial, sans-serif;
    font-weight: 700;
    font-size: 34px;
    fill: var(--label-blue);
  }
  .field-value-bold {
    font-family: "Open Sans", Arial, sans-serif;
    font-weight: 700;
    font-size: 31px;
    fill: var(--ink);
  }
  .field-value {
    font-family: "Open Sans", Arial, sans-serif;
    font-weight: 400;
    font-size: 29px;
    fill: var(--ink);
  }
  .contact-label {
    font-family: "Open Sans", Arial, sans-serif;
    font-weight: 700;
    font-size: 36px;
    fill: var(--accent-yellow);
  }
  .phone-number {
    font-family: "Open Sans", Arial, sans-serif;
    font-weight: 800;
    font-size: 60px;
    fill: var(--card-white);
  }
  .street-address {
    font-family: "Open Sans", Arial, sans-serif;
    font-weight: 600;
    font-size: 30px;
    fill: var(--card-white);
  }
</style>
</head>
<body>
<main class="business-card">
  <svg class="card-art" viewBox="0 0 1200 686" xmlns="http://www.w3.org/2000/svg">
    <defs>
      <linearGradient id="wave-fill" x1="0" y1="0" x2="1" y2="0">
        <stop offset="0" stop-color="var(--wave-lime)"/>
        <stop offset="0.4" stop-color="var(--wave-teal)"/>
        <stop offset="1" stop-color="var(--wave-blue)"/>
      </linearGradient>
    </defs>

    <g class="swoosh">
      <path class="swoosh-lime" d="M0,628 Q860,565 1200,0 L1200,686 L0,686 Z" fill="var(--accent-yellow)"/>
      <path class="swoosh-blue" d="M0,652 Q900,610 1200,78 L1200,686 L0,686 Z" fill="url(#wave-fill)"/>
    </g>

    <g class="brand">
      <circle class="brand-mark" cx="118" cy="112" r="52"/>
      <text class="brand-name" x="200" y="135">Blue Fern Commons</text>
    </g>

    <g class="contact-left">
      <text class="field-label" x="26" y="297">Name:</text>
      <text class="field-value-bold" x="171" y="297">Paula Whitcombe &amp; Darrell Whitcombe</text>

      <text class="field-label" x="26" y="389">Email ad:</text>
      <text class="field-value" x="231" y="389">paula@bluefernhome.com</text>
      <text class="field-value" x="231" y="426">darrell@bluefernhome.com</text>

      <text class="field-label" x="26" y="478">Web ad:</text>
      <text class="field-value-bold" x="203" y="478">bluefernhome.com</text>
    </g>

    <g class="contact-right">
      <text class="contact-label" x="972" y="463" text-anchor="middle">Phone:</text>
      <text class="phone-number" x="1176" y="539" text-anchor="end">281.604.2218</text>
      <text class="contact-label" x="791" y="608" text-anchor="middle">Address:</text>
      <text class="street-address" x="1176" y="657" text-anchor="end">1783 Wexford Lane, Porterfield, Texas 77812</text>
    </g>
  </svg>
</main>
</body>
</html>
```